Marova Hand Wash

Design hand washes. Total 12 variants to be designed.

Variants name are:

1) MILK &OLIVE
2) Shea Butter
3) Hidden Glow
4) Cream and Peach
5) Milk and Honey
6) Amber Riddle
7) Bakhour
8) Musk
9) White Oud
10) Black Oud
11) Rose Oud
12) Oud & Sandalwood

Labels can be on transparent sticker or background colors. All variants will be differentiated by fragrances and color. Bottle will be transparent. Pumps used for dispensing will be in Black or Transparent Color.

Designers can initially present designs of 4-5 variants initially. Later based on feedback, they can work out on more.

Bottle is 400ml and shape is rectangle. Ignore the size on bottle picture. Bottle keyline is attached.

Target Market(s)

B+, B, C+

Requirements
Must have
• Some relation to the variant names

```html
<!DOCTYPE html>
<html lang="en">
<head>
<meta charset="utf-8">
<title>Marova Hand Wash Labels</title>
<link rel="stylesheet" href="https://fonts.googleapis.com/css2?family=Pinyon+Script&family=Lora:wght@600&family=Montserrat:wght@500;600&display=swap">
<style>
  :root {
    --canvas: #ffffff;
    --label: #f7f7f8;
    --label-edge: #e4e4e7;
    --brand: #4b3a8c;
    --glow-ink: #e8365f;
    --shea-ink: #8a2e1c;
    --white: #ffffff;
  }
  * { margin: 0; padding: 0; box-sizing: border-box; }
  html, body { width: 1200px; height: 1101px; overflow: hidden; background: var(--canvas); }
  .canvas { position: relative; width: 1200px; height: 1101px; }
  .label {
    position: absolute; top: 259px; width: 420px; height: 746px;
    background: var(--label); border: 1px solid var(--label-edge);
    border-radius: 18px; overflow: hidden;
  }
  .label--glow { left: 150px; }
  .label--shea { left: 630px; }
  .brand {
    position: absolute; top: 90px; left: 0; right: 0; text-align: center;
    font-family: "Lora", serif; font-weight: 600; font-size: 54px; color: var(--brand);
  }
  .variant {
    position: absolute; top: 200px; left: 26px; right: 20px;
    font-family: "Pinyon Script", cursive; font-size: 104px; line-height: 0.98;
  }
  .variant--glow { color: var(--glow-ink); }
  .variant--shea { color: var(--shea-ink); }
  .variant span { display: block; }
  .variant span + span { padding-left: 16px; }
  .fragrance-art { position: absolute; right: 0; bottom: 0; width: 100%; height: 420px; }
  .fragrance-art--glow {
    background: radial-gradient(ellipse 75% 70% at 75% 80%, #e23fb0 0%, #ef5f8e 40%, rgba(240,110,170,0.45) 68%, rgba(247,247,248,0) 100%);
  }
  .fragrance-art--shea {
    background: radial-gradient(ellipse 75% 70% at 70% 80%, #ef6a5a 0%, #f3a06a 38%, rgba(240,150,170,0.45) 68%, rgba(247,247,248,0) 100%);
  }
  .volume, .product-type {
    position: absolute; right: 26px; color: var(--white);
    font-family: "Montserrat", sans-serif; font-weight: 600;
  }
  .volume { bottom: 80px; font-size: 34px; letter-spacing: 5px; }
  .product-type { bottom: 22px; font-size: 40px; letter-spacing: 10px; font-weight: 500; }
</style>
</head>
<body>
<main class="canvas">
  <section class="label label--glow">
    <div class="fragrance-art fragrance-art--glow" role="img" aria-label="Swirling pink and violet fragrance smoke"></div>
    <p class="brand">Marova</p>
    <h2 class="variant variant--glow"><span>Hidden</span><span>Glow</span></h2>
    <p class="volume">400ml</p>
    <p class="product-type">handwash</p>
  </section>
  <section class="label label--shea">
    <div class="fragrance-art fragrance-art--shea" role="img" aria-label="Swirling peach and coral fragrance smoke"></div>
    <p class="brand">Marova</p>
    <h2 class="variant variant--shea"><span>Shea</span><span>Butter</span></h2>
    <p class="volume">400ml</p>
    <p class="product-type">handwash</p>
  </section>
</main>
</body>
</html>
```